Business card design needed for Renewable utilities company based in New Zealand.

We supply and install solar panels and all components along with it for a fully customisable PV system that helps customer save money on their energy bills right away and also save the planet!

I have attached logo & website design files to give you a better insight.

Business

```html
<!DOCTYPE html>
<html lang="en">
<head>
<meta charset="utf-8">
<title>Kowhai Solar – Business Card</title>
<link rel="stylesheet" href="https://fonts.googleapis.com/css2?family=Open+Sans:wght@400;600&display=swap">
<style>
  :root {
    --page-bg: #e4e6ea;
    --card-white: #fbfbfb;
    --brand-blue: #24519b;
    --brand-blue-deep: #1a3f80;
    --brand-blue-light: #2f6bbd;
    --navy-text: #1f3d78;
    --grey-text: #5a5f66;
    --ink: #2b2f36;
  }
  * { box-sizing: border-box; margin: 0; padding: 0; }
  html, body { width: 1200px; height: 899px; overflow: hidden; }
  body {
    background: var(--page-bg);
    font-family: "Open Sans", Arial, sans-serif;
    display: flex;
    flex-direction: column;
    align-items: center;
    justify-content: center;
    gap: 48px;
  }
  .card {
    width: 640px;
    height: 366px;
    position: relative;
    overflow: hidden;
    box-shadow: 0 6px 18px rgba(0,0,0,0.18);
  }

  /* Brand block */
  .brand {
    position: absolute;
    left: 0; right: 0;
    display: flex;
    flex-direction: column;
    align-items: center;
  }
  .brand__mark {
    width: 78px; height: 78px;
    border-radius: 50%;
    background: var(--brand-blue);
  }
  .brand__name {
    font-family: "Open Sans", Arial, sans-serif;
    font-weight: 600;
    color: var(--navy-text);
    font-size: 34px;
    margin-top: 14px;
    white-space: nowrap;
  }

  /* Front */
  .card--front { background: var(--card-white); }
  .card--front .brand { top: 34px; }
  .person {
    position: absolute;
    top: 196px; left: 0; right: 0;
    text-align: center;
  }
  .person__name {
    font-weight: 600;
    color: var(--navy-text);
    font-size: 22px;
  }
  .person__title {
    color: var(--grey-text);
    font-size: 13px;
    margin-top: 2px;
  }
  .contacts {
    position: absolute;
    display: flex;
    flex-direction: column;
    gap: 3px;
    font-size: 13.5px;
    color: var(--ink);
    white-space: nowrap;
  }
  .contacts--phones { left: 70px; top: 270px; }
  .contacts--web { right: 70px; top: 262px; }
  .contact { display: flex; align-items: center; gap: 7px; }
  .contact svg { width: 14px; height: 14px; flex: none; }
  .tagline-band {
    position: absolute;
    left: 0; right: 0; bottom: 0;
    height: 40px;
    background: var(--brand-blue);
    color: #fff;
    font-size: 16px;
    display: flex;
    align-items: center;
    justify-content: center;
  }

  /* Back */
  .card--back {
    background: radial-gradient(ellipse at 45% 40%, var(--brand-blue-light) 0%, var(--brand-blue) 55%, var(--brand-blue-deep) 100%);
  }
  .card--back .brand { top: 86px; }
  .card--back .brand__mark { width: 104px; height: 104px; background: #fff; }
  .card--back .brand__name { color: #fff; font-size: 42px; margin-top: 16px; }
  .back__web {
    position: absolute;
    left: 0; right: 0; top: 290px;
    text-align: center;
    color: #fff;
    font-size: 17px;
    letter-spacing: 0.3px;
  }
</style>
</head>
<body>

<section class="card card--front">
  <div class="brand">
    <div class="brand__mark"></div>
    <div class="brand__name">Kowhai Solar</div>
  </div>

  <div class="person">
    <div class="person__name">Alex Rowan Tait</div>
    <div class="person__title">General Manager</div>
  </div>

  <div class="contacts contacts--phones">
    <div class="contact">
      <svg viewBox="0 0 14 14" aria-hidden="true"><rect x="3" y="0.5" width="8" height="13" rx="2" fill="var(--navy-text)"/><rect x="4.5" y="2.5" width="5" height="7" fill="#fff"/></svg>
      <span>(03) 481 2907</span>
    </div>
    <div class="contact">
      <svg viewBox="0 0 14 14" aria-hidden="true"><circle cx="7" cy="7" r="7" fill="var(--navy-text)"/><rect x="3.5" y="5.5" width="7" height="5" rx="1" fill="#fff"/><path d="M3 5 Q7 2 11 5" stroke="#fff" stroke-width="1.4" fill="none"/></svg>
      <span>0508 764 219</span>
    </div>
  </div>

  <div class="contacts contacts--web">
    <div class="contact">
      <svg viewBox="0 0 14 14" aria-hidden="true"><circle cx="7" cy="7" r="7" fill="var(--navy-text)"/><rect x="3" y="4.5" width="8" height="5.5" fill="#fff"/><path d="M3 4.5 L7 8 L11 4.5" stroke="var(--navy-text)" stroke-width="1" fill="none"/></svg>
      <span>hello@kowhaisolar.co.nz</span>
    </div>
    <div class="contact">
      <svg viewBox="0 0 14 14" aria-hidden="true"><circle cx="7" cy="7" r="7" fill="var(--navy-text)"/><circle cx="7" cy="7" r="4.5" fill="none" stroke="#fff" stroke-width="1"/><ellipse cx="7" cy="7" rx="2" ry="4.5" fill="none" stroke="#fff" stroke-width="1"/><line x1="2.5" y1="7" x2="11.5" y2="7" stroke="#fff" stroke-width="1"/></svg>
      <span>www.kowhaisolar.co.nz</span>
    </div>
  </div>

  <div class="tagline-band">This can be a tag line text or office address</div>
</section>

<section class="card card--back" role="img" aria-label="Blue card back with a faint dotted world map behind the brand name">
  <div class="brand">
    <div class="brand__mark"></div>
    <div class="brand__name">Kowhai Solar</div>
  </div>
  <div class="back__web">www.kowhaisolar.co.nz</div>
</section>

</body>
</html>
```